Plume & Crest Hair Extensions needs a business card

We need a business card designed for an online luxury hair extensions business called Plume & Crest, we already have a logo and need an innovative business card (2-sided preferably). The strap line for the brand is 'Luxury Hair At Every Touchpoint!'. The brand is a premium brand selling virgin hair extensions and the target market is the mid-affluent ethnic woman as such the design should reflect this. The brand logo is grey and can be sent when requested.

Target Market(s)

25 to 35 year mid-affluent ethnic woman (Afro-American, Mixed Race, Asian)

Industry/Entity Type

Hair

Colors

Designer to choose colors to be used in the design.

Requirements
Must have
• Business Name: Plume and Crest
Strapline: Luxury hair at every touchpoint!
Domain: ​www.plumeandcrest.example
Email: info@plumeandcrest.example
sales and enquiries
44 07500 xxxxxxx

Please use the grey main brand logo depicted in page 2 of the attached pdf document

```html
<!DOCTYPE html>
<html lang="en">
<head>
<meta charset="utf-8">
<title>Plume &amp; Crest — Business Card</title>
<link href="https://fonts.googleapis.com/css2?family=Pinyon+Script&family=Didact+Gothic&display=swap" rel="stylesheet">
<style>
  :root {
    --bg: #2a2a2a;
    --ink: #0b0b0b;
    --cream: #f3f1dc;
    --cream-soft: #dcdac4;
    --line: #e8e6d0;
  }
  * { margin: 0; padding: 0; box-sizing: border-box; }
  html, body {
    width: 1200px;
    height: 1000px;
    overflow: hidden;
    background: var(--bg);
  }
  .canvas {
    position: relative;
    width: 1200px;
    height: 1000px;
  }
  .card {
    position: absolute;
    left: 220px;
    width: 760px;
    height: 430px;
    overflow: hidden;
    box-shadow: 0 18px 40px rgba(0,0,0,0.55);
  }
  .card--front { top: 60px; background: var(--cream); }
  .card--back  { top: 510px; background: var(--ink); }

  .card__shape { position: absolute; inset: 0; }

  /* Front side: brand lockup */
  .brand {
    position: absolute;
    left: 70px;
    top: 200px;
    display: flex;
    align-items: center;
    gap: 20px;
  }
  .brand__square {
    width: 56px;
    height: 56px;
    background: var(--ink);
  }
  .brand__name {
    font-family: "Didact Gothic", sans-serif;
    font-size: 40px;
    line-height: 1;
    color: var(--ink);
    letter-spacing: 1px;
    white-space: nowrap;
  }
  .offer {
    position: absolute;
    right: 30px;
    top: 58px;
    font-family: "Pinyon Script", cursive;
    font-size: 46px;
    line-height: 1.05;
    color: var(--cream);
  }
  .offer span { display: block; padding-left: 70px; }

  /* Back side */
  .plume-art {
    position: absolute;
    left: 0;
    top: 130px;
    width: 270px;
    height: 300px;
    border-top-right-radius: 140px;
    background: radial-gradient(ellipse at 30% 70%, var(--cream) 0%, var(--cream-soft) 55%, #6e6d62 100%);
  }
  .contact {
    position: absolute;
    left: 330px;
    top: 40px;
    width: 400px;
    text-align: center;
    color: var(--line);
  }
  .contact__strap {
    font-family: "Pinyon Script", cursive;
    font-size: 52px;
    line-height: 1.1;
  }
  .contact__sub {
    font-family: "Didact Gothic", sans-serif;
    font-size: 26px;
    margin-top: 4px;
  }
  .contact__rule {
    width: 260px;
    height: 2px;
    margin: 30px auto 34px;
    background: linear-gradient(90deg, transparent, var(--line) 45%, var(--line) 55%, transparent);
  }
  .contact__list {
    list-style: none;
    font-family: "Didact Gothic", sans-serif;
    font-size: 21px;
    line-height: 1.45;
  }
</style>
</head>
<body>
<main class="canvas">

  <section class="card card--front" aria-label="Business card, front">
    <svg class="card__shape" viewBox="0 0 760 430" aria-hidden="true">
      <path d="M330 0 C 420 120, 560 230, 700 430 L760 430 L760 0 Z" fill="#0b0b0b"/>
    </svg>
    <div class="brand">
      <span class="brand__square" aria-hidden="true"></span>
      <span class="brand__name">Plume &amp; Crest</span>
    </div>
    <p class="offer">Online luxury<span>Hair extensions</span></p>
  </section>

  <section class="card card--back" aria-label="Business card, back">
    <div class="plume-art" role="img" aria-label="Flowing hair illustration"></div>
    <div class="contact">
      <p class="contact__strap">Luxury Hair</p>
      <p class="contact__sub">At Every Touchpoint!</p>
      <div class="contact__rule"></div>
      <ul class="contact__list">
        <li>www.plumeandcrest.example</li>
        <li>Email: info@plumeandcrest.example</li>
        <li>Tel: (44) 07500 118204</li>
      </ul>
    </div>
  </section>

</main>
</body>
</html>
```